Home inspection business! professional look attracting customers just by looks. Read must haves

its a new business I started on my own for home inspections I would like something very professional to give to real estate agents and clients, its going to have my license number on it my business phone number my name my website as well etc on the back side it will be servicing areas and also what kind of services I offer I also have a business card from someone else the way I would like mine to be. I will attach my logo

Home Inspection

listed in nice to haves

• phone number - 555 293 8471
• website- hollowpinecheck.com
• license number #2938475610
• my name Gavin keropulis
• picture of my logo and me on the front
• on the back of the card. stating I am servicing All of New York and Long Island
• also services I will offer will be home inspection -mold inspection -lead inspection -radon inspection -Termite Inspection -Infared Scan.
• and also we provide inspections for single family homes condos co-ops town-homes
• and commercial property
• same colors as the logos and also if you recommend fonts to look like the logo not sure up to you

```html
<!DOCTYPE html>
<html lang="en">
<head>
<meta charset="UTF-8">
<title>Hollow Pine Home Inspectors – Business Card</title>
<link href="https://fonts.googleapis.com/css2?family=Roboto:wght@400;500;700&display=swap" rel="stylesheet">
<style>
  :root {
    --page: #ffffff;
    --paper: #f3f3f2;
    --navy: #03559a;
    --sky: #22abf7;
    --ink: #383838;
    --ink-soft: #5a5a5a;
    --ghost: #cfdbe6;
    --white: #ffffff;
  }
  * { margin: 0; padding: 0; box-sizing: border-box; }
  html, body {
    width: 1121px; height: 1200px; overflow: hidden;
    background: var(--page);
    font-family: "Roboto", Arial, sans-serif;
    color: var(--ink);
  }
  .canvas { position: relative; width: 1121px; height: 1200px; }

  .card {
    position: absolute; left: 140px; width: 841px;
    background: var(--paper);
    overflow: hidden;
  }
  .card--front { top: 118px; height: 468px; }
  .card--back  { top: 614px; height: 467px; }

  /* Front */
  .brand { position: absolute; left: 44px; top: 150px; }
  .brand__row { display: flex; align-items: center; gap: 12px; }
  .brand__dot {
    width: 30px; height: 30px; border-radius: 50%;
    background: var(--sky);
  }
  .brand__name {
    font-weight: 700; font-size: 40px; letter-spacing: 0.5px;
    color: var(--ink-soft); text-transform: uppercase; line-height: 1;
  }
  .brand__tagline {
    margin-top: 14px; margin-left: 42px;
    font-size: 19px; font-weight: 500; letter-spacing: 11.6px;
    color: var(--ink-soft); text-transform: uppercase;
  }

  .contact { position: absolute; left: 88px; top: 266px; font-weight: 500; }
  .contact__phone { font-size: 27px; letter-spacing: 0.6px; line-height: 1; }
  .contact__area { font-size: 27px; letter-spacing: 0.3px; margin-top: 13px; line-height: 1; }
  .contact__license { font-size: 20px; letter-spacing: 1px; margin-top: 16px; line-height: 1; }

  .profile__strip {
    position: absolute; left: 593px; top: 0; width: 187px; height: 399px;
    background: var(--sky);
  }
  .profile__photo {
    position: absolute; left: 573px; top: 49px; width: 227px; height: 273px;
    background: linear-gradient(180deg, #3d5a3a 0%, #587a52 35%, #4f8fbf 65%, #3a7fb5 100%);
  }
  .profile__name {
    position: absolute; left: 593px; top: 330px; width: 187px;
    text-align: center; color: var(--white);
    font-weight: 700; font-size: 24px; letter-spacing: 1.2px; line-height: 25px;
  }

  .web-band {
    position: absolute; left: 0; bottom: 0; width: 100%; height: 69px;
    background: var(--navy);
    display: flex; justify-content: center; padding-top: 9px;
  }
  .web-band__url {
    color: var(--white); font-weight: 700; font-size: 29px; letter-spacing: 3px;
  }

  /* Back */
  .band { position: absolute; left: 0; width: 100%; height: 33px; background: var(--navy); }
  .band--top { top: 0; }
  .band--bottom { bottom: 0; }

  .ghost-mark { position: absolute; left: 68px; top: 93px; width: 360px; height: 302px; }
  .ghost-mark__ring {
    position: absolute; left: 0; top: 0; width: 302px; height: 302px;
    border-radius: 50%; border: 26px solid var(--ghost);
  }
  .ghost-mark__name {
    position: absolute; left: 20px; top: 134px; width: 262px; text-align: center;
    font-weight: 700; font-size: 32px; color: var(--ghost);
    text-transform: uppercase; letter-spacing: 1px;
  }

  .services { position: absolute; left: 464px; top: 92px; }
  .services__title { font-weight: 500; font-size: 30px; letter-spacing: 0.8px; line-height: 1; }
  .services__list { list-style: none; margin-top: 18px; }
  .services__item {
    font-weight: 500; font-size: 30px; letter-spacing: 0.8px;
    line-height: 37.7px;
  }
</style>
</head>
<body>
<div class="canvas">

  <section class="card card--front">
    <div class="brand">
      <div class="brand__row">
        <span class="brand__dot"></span>
        <span class="brand__name">Hollow Pine</span>
      </div>
      <div class="brand__tagline">Home Inspectors</div>
    </div>

    <div class="contact">
      <p class="contact__phone">Phone: 555 293 8471</p>
      <p class="contact__area">New York and Long Island</p>
      <p class="contact__license">License: #2938475610</p>
    </div>

    <div class="profile__strip"></div>
    <div class="profile__photo" role="img" aria-label="Portrait photo of the home inspector outdoors"></div>
    <p class="profile__name">Gavin<br>Keropulis</p>

    <div class="web-band"><span class="web-band__url">www.hollowpinecheck.com</span></div>
  </section>

  <section class="card card--back">
    <div class="band band--top"></div>

    <div class="ghost-mark" aria-hidden="true">
      <div class="ghost-mark__ring"></div>
      <div class="ghost-mark__name">Hollow Pine</div>
    </div>

    <div class="services">
      <h2 class="services__title">Inspections Offered:</h2>
      <ul class="services__list">
        <li class="services__item">All types of homes</li>
        <li class="services__item">Commercial property</li>
        <li class="services__item">Mold</li>
        <li class="services__item">Lead</li>
        <li class="services__item">Radon</li>
        <li class="services__item">Termite</li>
        <li class="services__item">Infrared Scan</li>
      </ul>
    </div>

    <div class="band band--bottom"></div>
  </section>

</div>
</body>
</html>
```